Voltarey - Flyer design

Description -
Motorhome and Caravan EWOFs
Recreational Vehicles (such as caravans, motorhomes, RVs, Boats etc) and Relocatable buildings that can be connected to an electricity supply must be regularly checked for electrical safety. An EWOF needs to be issued every 4 years.
Pre-purchase house inspections
A pre-purchase electrical inspection prior to buying a home can be used to identify any dangerous and unsafe electrical parts of the installation that may be costly to repair once the property has been purchased. Giving you peace of mind when buying your new home.
High risk Electrical inspections
All Prescribed Electrical Work that falls under the High Risk category must be inspected by a Registered Electrical Inspector and have a Record of Inspection certificate issued.
Electric Vehicle Chargers
Any electrical vehicle charger that can be accessed by the public (ie in a non-domestic situation) must be periodically inspected and certified every 12 months.
General Electrical Services
Domestic and commercial - We do new builds, Renovations, Maintenance and more!
Dean Fowler - Electrician and Electrical Inspector
Ph - 0227839152
Dean@voltarey.co.nz
Auckland
------
I also want there to be a few symbols similar to the files I have attached.
The main areas that I am hoping to find work is with caravans/motohomes and EV car chargers so these symbols are quite important.
Thanks so much

```html
<!DOCTYPE html>
<html lang="en">
<head>
<meta charset="utf-8">
<title>Voltarey – Flyer</title>
<link rel="stylesheet" href="https://fonts.googleapis.com/css2?family=Montserrat:wght@700;800&family=Poppins:wght@400;500;600;700&display=swap">
<style>
  :root{
    --green:#8cc63f;
    --dark:#2b2b2b;
    --charcoal:#3a3a3a;
    --white:#ffffff;
    --ink:#1e1e1e;
  }
  *{margin:0;padding:0;box-sizing:border-box}
  html,body{width:945px;height:1200px;overflow:hidden;background:var(--white)}
  body{font-family:"Poppins",sans-serif;color:var(--ink)}
  .flyer{position:relative;width:945px;height:1200px;background:var(--white);overflow:hidden}
  .abs{position:absolute}

  .green-panel{left:446px;top:0;width:499px;height:1016px;background:var(--green)}

  .brand{left:64px;top:78px}
  .brand-name{font-family:"Poppins",sans-serif;font-weight:500;font-size:38px;line-height:46px;color:var(--charcoal);letter-spacing:-.5px}

  .hero{left:110px;top:180px;width:778px;height:316px;background:linear-gradient(90deg,#1f1f1f,#3a3a3a 70%,#444);box-shadow:0 0 0 6px #3a3a3a inset}
  .plug-art{left:0;top:176px;width:176px;height:318px;background:linear-gradient(160deg,#3a3a3a,#111);border-radius:0 90px 90px 0}
  .worker-photo{left:580px;top:204px;width:298px;height:292px;background:linear-gradient(135deg,#8a8a8a,#5b5b5b 55%,#2f3a55)}
  .headline{left:197px;top:235px;font-family:"Montserrat",sans-serif;font-weight:800;font-size:32px;line-height:36px;color:var(--white)}
  .headline .accent{color:var(--green)}
  .dots{left:198px;top:392px;display:flex;gap:4px}
  .dots span{width:5px;height:5px;border-radius:50%;background:var(--green)}
  .subhead{left:197px;top:410px;font-family:"Poppins",sans-serif;font-weight:500;font-size:17.5px;line-height:23px;color:var(--white)}

  .thumb{top:505px;width:153px;height:132px;border:4px solid var(--charcoal)}
  .thumb-motorhome{left:397px;background:linear-gradient(180deg,#c9dbe8 0%,#d8cfbd 45%,#6f9a3c 100%)}
  .thumb-van{left:567px;background:linear-gradient(180deg,#5d7a3e 0%,#f1f1f1 50%,#8a9a4e 100%)}
  .thumb-boat{left:736px;background:linear-gradient(180deg,#8fbde0 0%,#f2f2f2 50%,#3c7fb0 100%)}

  .section-title{left:77px;top:545px;font-family:"Montserrat",sans-serif;font-weight:800;font-size:34px;line-height:36px;letter-spacing:4px;color:var(--dark)}

  .service-card{left:77px;width:272px;border:3px solid var(--green);border-radius:18px}
  .card-ev{top:637px;height:236px}
  .card-general{top:909px;height:234px}
  .card-title{font-family:"Montserrat",sans-serif;font-weight:800;font-size:22.5px;line-height:29px;color:var(--green)}
  .card-text{font-size:13.4px;line-height:17px;color:var(--ink)}
  .card-sub{font-weight:600;font-size:14.5px;color:var(--ink)}
  .ticks{list-style:none;font-size:13.5px;line-height:22px}
  .ticks li{display:flex;align-items:flex-start;gap:6px}
  .ticks li::before{content:"";flex:none;width:8px;height:8px;margin-top:7px;border-radius:50%;background:var(--green)}
  .card-plug{right:-12px;top:-15px;background:var(--white);padding-left:4px}

  .svc-icon{left:414px;width:60px;height:60px;border-radius:50%;background:var(--dark);border:4px solid var(--white);display:flex;align-items:center;justify-content:center}
  .svc-title{left:493px;font-family:"Poppins",sans-serif;font-weight:600;font-size:18px;color:var(--dark)}
  .svc-text{left:490px;width:385px;font-size:11.6px;line-height:14.4px;color:var(--ink)}

  .contact-title{left:420px;top:1030px;font-family:"Poppins",sans-serif;font-weight:600;font-size:30px;color:var(--dark)}
  .name-tag{left:423px;top:1076px;height:38px;display:flex}
  .name-tag .name{background:var(--dark);color:var(--white);font-family:"Poppins",sans-serif;font-weight:700;font-size:21px;padding:0 12px;display:flex;align-items:center}
  .name-tag .role{background:var(--green);color:var(--dark);font-weight:600;font-size:11px;line-height:13px;padding:0 14px 0 12px;margin-left:3px;display:flex;align-items:center}
  .contact-row{left:420px;top:1128px;display:flex;gap:22px;font-size:15px;color:var(--dark)}
  .contact-row span{display:flex;align-items:center;gap:5px}
</style>
</head>
<body>
<div class="flyer">
  <div class="abs green-panel"></div>

  <div class="abs brand"><div class="brand-name">Voltarey</div></div>

  <div class="abs hero"></div>
  <div class="abs plug-art" role="img" aria-label="Black electrical plug with curled cable"></div>
  <div class="abs worker-photo" role="img" aria-label="Electrician in hard hat working on a wall socket"></div>
  <h1 class="abs headline">YOUR TRUSTED<br>PARTNER IN<br><span class="accent">ELECTRICAL SAFETY<br>AND COMPLIANCE</span></h1>
  <div class="abs dots"><span></span><span></span><span></span><span></span><span></span></div>
  <p class="abs subhead">Your Trusted Experts in Electrical<br>Compliance and Repairs</p>

  <div class="abs thumb thumb-motorhome" role="img" aria-label="Vintage motorhome on grass"></div>
  <div class="abs thumb thumb-van" role="img" aria-label="White camper van in the countryside"></div>
  <div class="abs thumb thumb-boat" role="img" aria-label="Motor yacht moored in a marina"></div>

  <h2 class="abs section-title">OUR<br>SERVICES</h2>

  <div class="abs service-card card-ev">
    <svg class="abs card-plug" width="42" height="26" viewBox="0 0 42 26" aria-hidden="true"><g fill="var(--green)"><rect x="0" y="11" width="16" height="4"/><rect x="14" y="4" width="14" height="18" rx="3"/><rect x="27" y="6" width="12" height="4"/><rect x="27" y="16" width="12" height="4"/></g></svg>
    <div class="abs card-title" style="left:26px;top:20px">Electric<br>Vehicle<br>Chargers</div>
    <p class="abs card-text" style="left:26px;top:120px;width:238px">Any electrical vehicle charger that can be accessed by the public (ie in a non-domestic situation) must be periodically inspected and certified every 12 months.</p>
    <svg class="abs" style="right:-14px;bottom:-30px;background:var(--white)" width="84" height="60" viewBox="0 0 84 60" aria-hidden="true"><g fill="var(--green)"><path d="M16 4h52l10 22v28H6V26z"/></g><g fill="var(--white)"><path d="M20 10h44l7 16H13z"/><circle cx="17" cy="36" r="5"/><circle cx="67" cy="36" r="5"/></g><rect x="6" y="48" width="72" height="4" fill="var(--white)"/></svg>
  </div>

  <div class="abs service-card card-general">
    <svg class="abs card-plug" width="42" height="26" viewBox="0 0 42 26" aria-hidden="true"><g fill="var(--green)"><rect x="0" y="11" width="16" height="4"/><rect x="14" y="4" width="14" height="18" rx="3"/><rect x="27" y="6" width="12" height="4"/><rect x="27" y="16" width="12" height="4"/></g></svg>
    <div class="abs card-title" style="left:26px;top:20px">General Electrical<br>Services</div>
    <div class="abs card-sub" style="left:26px;top:82px">Domestic and commercial</div>
    <div class="abs card-text" style="left:30px;top:110px">We do</div>
    <ul class="abs ticks" style="left:30px;top:130px">
      <li>New builds</li><li>Renovations</li><li>Maintenance<br>and more!</li>
    </ul>
    <svg class="abs" style="right:-6px;top:145px;background:var(--white)" width="80" height="84" viewBox="0 0 80 84" aria-hidden="true"><g fill="none" stroke="var(--green)" stroke-width="3.5"><path d="M40 4a38 38 0 1 1-30 62"/><path d="M16 38L36 18l20 20v26H16z"/><path d="M36 32a8 8 0 0 1 5 14v4h-10v-4a8 8 0 0 1 5-14z"/></g></svg>
  </div>

  <div class="abs svc-icon" style="top:656px"><svg width="30" height="24" viewBox="0 0 30 24" aria-hidden="true"><g fill="none" stroke="#fff" stroke-width="2.2"><rect x="2" y="3" width="22" height="15" rx="2"/><path d="M24 8h3l2 4v6h-5"/><rect x="6" y="7" width="6" height="4"/></g><circle cx="8" cy="20" r="2.5" fill="#fff"/><circle cx="22" cy="20" r="2.5" fill="#fff"/></svg></div>
  <h3 class="abs svc-title" style="top:662px">Motorhome and Caravan EWOFs</h3>
  <p class="abs svc-text" style="top:692px">Recreational Vehicles (such as caravans, motorhomes, RVs, Boats etc) and Relocatable buildings that can be connected to an electricity supply must be regularly checked for electrical safety. An EWOF needs to be issued every 4 years.</p>

  <div class="abs svc-icon" style="top:772px"><svg width="30" height="30" viewBox="0 0 30 30" aria-hidden="true"><g fill="none" stroke="#fff" stroke-width="2.2"><path d="M3 14L14 4l11 10"/><path d="M6 12v12h8"/><circle cx="20" cy="20" r="5"/><path d="M24 24l4 4"/><path d="M18 20l2 2 3-3"/></g></svg></div>
  <h3 class="abs svc-title" style="top:778px">Pre-purchase house inspections</h3>
  <p class="abs svc-text" style="top:809px">A pre-purchase electrical inspection prior to buying a home can be used to identify any dangerous and unsafe electrical parts of the installation that may be costly to repair once the property has been purchased. Giving you peace of mind when buying your new home.</p>

  <div class="abs svc-icon" style="top:904px"><svg width="30" height="30" viewBox="0 0 30 30" aria-hidden="true"><g fill="none" stroke="#fff" stroke-width="2.2"><path d="M3 14L15 3l12 11"/><path d="M6 12v15h18V12"/><circle cx="15" cy="19" r="5"/><path d="M13 16v3M17 16v3"/></g></svg></div>
  <h3 class="abs svc-title" style="top:911px">High risk Electrical inspections</h3>
  <p class="abs svc-text" style="top:940px">All Prescribed Electrical Work that falls under the High Risk category must be inspected by a Registered Electrical Inspector and have a Record of Inspection certificate issued.</p>

  <h2 class="abs contact-title">Contact Us Today!</h2>
  <div class="abs name-tag"><div class="name">DEAN FOWLER</div><div class="role">Electrician and<br>Electrical Inspector</div></div>
  <div class="abs contact-row">
    <span><svg width="16" height="16" viewBox="0 0 16 16" aria-hidden="true"><circle cx="8" cy="8" r="8" fill="var(--green)"/><path d="M5 4l2 2-1 1.5a6 6 0 0 0 2.5 2.5L10 9l2 2-1.5 1.5C7 12 4 9 3.5 5.5z" fill="var(--dark)"/></svg>0227839152</span>
    <span><svg width="16" height="16" viewBox="0 0 16 16" aria-hidden="true"><circle cx="8" cy="8" r="8" fill="var(--green)"/><rect x="4" y="5" width="8" height="6" fill="var(--dark)"/><path d="M4 5l4 3 4-3" stroke="var(--green)" fill="none"/></svg>Dean@voltarey.co.nz</span>
    <span><svg width="16" height="16" viewBox="0 0 16 16" aria-hidden="true"><circle cx="8" cy="8" r="8" fill="var(--green)"/><path d="M8 3a3 3 0 0 1 3 3c0 2-3 6-3 6S5 8 5 6a3 3 0 0 1 3-3z" fill="var(--dark)"/></svg>Auckland</span>
  </div>
</div>
</body>
</html>
```